BRENLO CAPITAL INSTITUTIONAL PRESENTATION

To create a powerpoint presentation with selected art and text.
Target Market(s)
Potential Investors for the fund
Industry/Entity Type
Finance
Font styles to use
Sans Serif
Colors
0692cd
0255a3
Requirements
Must have
- Unique art, to look sober and professional
Nice to have
- Modern look
Should not have
- Red as color...

```html
<!DOCTYPE html>
<html lang="en">
<head>
<meta charset="utf-8">
<title>Brenlo Capital — Institutional Presentation</title>
<link href="https://fonts.googleapis.com/css2?family=Open+Sans:wght@400;600;700&display=swap" rel="stylesheet">
<style>
:root{
  --blue:#0692cd;
  --navy:#0255a3;
  --sky:#2f9fe0;
  --ink:#222;
  --muted:#555;
  --line:#c9c9c9;
  --stage-light:#f4f4f4;
  --stage-dark:#bdbdbd;
  --photo-steel:#7d8f9c;
}
*{box-sizing:border-box;margin:0;padding:0}
html,body{width:1200px;height:1200px;overflow:hidden}
body{background:radial-gradient(circle at 50% 50%,var(--stage-light) 0%,#dedede 55%,var(--stage-dark) 100%);font-family:"Open Sans",sans-serif;color:var(--ink);position:relative}
.slide{position:absolute;width:330px;height:186px;background:#fff;overflow:hidden;box-shadow:3px 4px 6px rgba(0,0,0,.35)}
.slide *{position:absolute}
.c1{left:46px}.c2{left:441px}.c3{left:826px}
.r1{top:45px}.r2{top:266px}.r3{top:502px}.r4{top:733px}.r5{top:973px}

.brand{left:50%;bottom:6px;transform:translateX(-50%);font-size:6.5px;font-weight:600;color:var(--navy);white-space:nowrap}
.brand.light{color:#fff}

.heading{top:20px;left:0;display:flex;align-items:center;gap:6px;font-size:8px;color:var(--ink)}
.heading>*{position:static}
.heading .tab{width:7px;height:9px;background:var(--blue)}
.heading .tab.grey{background:#888}
.titlebox{top:20px;height:11px;border:1px solid var(--line);font-size:7px;line-height:9px;padding:0 4px;color:var(--ink);white-space:nowrap}
.titlebox.left{left:12px;width:306px}
.titlebox.right{right:12px;width:300px;text-align:right}
.titlebox .flag{position:absolute;top:-1px;width:6px;height:11px;background:var(--blue)}
.titlebox.left .flag{left:-8px;background:#888}
.titlebox.right .flag{right:-8px}

.photo{background:linear-gradient(160deg,#a9b9c4 0%,var(--photo-steel) 45%,#5b6b60 100%)}
.photo.sky{background:linear-gradient(180deg,#c5d2dc 0%,#8b9aa5 50%,#4f5a62 100%)}
.photo.tinted{background:linear-gradient(180deg,#4ea6dc,#1b78bf)}
.photo.dark{background:linear-gradient(180deg,#5a5f63,#3a3e41)}

.tiny{font-size:4.4px;line-height:5.6px;color:var(--muted)}
.small{font-size:5.2px;line-height:6.6px;color:var(--muted)}
.blue{color:var(--blue)}
.white{color:#fff}

.member{top:48px;width:70px;text-align:center}
.member .face{position:relative;display:block;margin:0 auto;width:30px;height:30px;border-radius:50%;background:radial-gradient(circle at 50% 40%,#b59a86,#5b5050 70%,#333)}
.member .name{position:relative;display:block;margin-top:5px;font-size:6.3px;color:var(--ink)}
.member .role{position:relative;display:block;margin-top:4px;font-size:5.2px;color:var(--blue)}
.member .role.sm{font-size:4.2px}

.agenda-list{left:146px;top:40px;width:146px;height:100px;background:#e4e4e4;padding:4px 4px 0 0}
.agenda-list div{position:relative;text-align:right;font-size:6.8px;line-height:15.5px;color:var(--ink)}
.agenda-list span{color:var(--blue);margin-left:3px}

.label-tab{height:8px;font-size:5.5px;line-height:8px;text-align:center;color:#fff;font-weight:700}
.icon{width:18px;height:18px;border-radius:50%;background:var(--navy);display:flex;align-items:center;justify-content:center}
.icon svg{position:static}
.svc{font-size:4px;line-height:5px;color:var(--muted);width:110px}
.svc b{display:block;color:var(--ink);font-weight:700;position:relative}
</style>
</head>
<body>

<section class="slide c1 r1" style="background:linear-gradient(135deg,#2b9de0,#1b7fc9)">
  <div class="photo" role="img" aria-label="Building facade and trees tinted blue" style="inset:0;background:linear-gradient(120deg,rgba(255,255,255,.18),rgba(6,146,205,.15) 50%,rgba(30,110,60,.3))"></div>
  <div class="brand light" style="left:30px;top:78px;bottom:auto;transform:none;font-size:12px">BRENLO CAPITAL</div>
  <div style="left:76px;top:99px;font-size:6px;font-weight:600;color:#fff">January 2018</div>
  <div style="left:244px;top:138px;font-size:10px;font-weight:700;color:#fff">TITLE</div>
</section>

<section class="slide c2 r1">
  <div class="heading"><span class="tab"></span><span>AGENDA</span></div>
  <div class="photo" role="img" aria-label="Office building with trees" style="left:41px;top:40px;width:100px;height:100px;border-top:3px solid var(--blue)"></div>
  <div class="agenda-list">
    <div>SUBJECT<span>01</span></div><div>SUBJECT<span>02</span></div><div>SUBJECT<span>03</span></div>
    <div>SUBJECT<span>04</span></div><div>SUBJECT<span>05</span></div><div>SUBJECT<span>06</span></div>
  </div>
  <div class="brand">BRENLO CAPITAL</div>
</section>

<section class="slide c3 r1">
  <div class="heading"><span class="tab"></span><span>OUR TEAM</span></div>
  <div class="member" style="left:18px"><span class="face" role="img" aria-label="Portrait photo"></span><span class="name">JORDAN LYLE</span><span class="role">CEO</span></div>
  <div class="member" style="left:89px"><span class="face" role="img" aria-label="Portrait photo"></span><span class="name">JORDAN LYLE</span><span class="role">SALESMAN</span></div>
  <div class="member" style="left:160px"><span class="face" role="img" aria-label="Portrait photo"></span><span class="name">JORDAN LYLE</span><span class="role sm">ACCOUNTMANAGER</span></div>
  <div class="member" style="left:236px"><span class="face" role="img" aria-label="Portrait photo"></span><span class="name">JORDAN LYLE</span><span class="role sm">ACCOUNTMANAGER</span></div>
  <div class="blue" style="left:25px;top:125px;font-size:4.6px;font-weight:700">WHAT DO WE DO</div>
  <div class="tiny" style="left:25px;top:133px;width:285px">Our products seek to generate returns in a wide range of markets without any preference for Asset Class or Market Direction (Long or Short). The investment team has a solid track record, and generated Alpha at the Interest Rates, Currency and Stock Markets.</div>
  <div class="tiny" style="left:25px;top:149px;width:285px">The investment universe is mainly made by: Brazil, Emerging Markets and the major economies such as USA, Japan and Europe.</div>
  <div class="brand">BRENLO CAPITAL</div>
</section>

<section class="slide c1 r2">
  <div class="heading"><span class="tab"></span><span>OUR TEAM</span></div>
  <div class="member" style="left:18px"><span class="face" role="img" aria-label="Portrait photo"></span><span class="name">JORDAN LYLE</span><span class="role">CEO</span></div>
  <div class="member" style="left:89px"><span class="face" role="img" aria-label="Portrait photo"></span><span class="name">JORDAN LYLE</span><span class="role">SALESMAN</span></div>
  <div class="member" style="left:161px"><span class="face" role="img" aria-label="Portrait photo"></span><span class="name">JORDAN LYLE</span><span class="role sm">ACCOUNTMANAGER</span></div>
  <div class="member" style="left:237px"><span class="face" role="img" aria-label="Portrait photo"></span><span class="name">JORDAN LYLE</span><span class="role sm">ACCOUNTMANAGER</span></div>
  <div class="blue" style="left:25px;top:125px;font-size:4.6px;font-weight:700">WHAT DO WE DO</div>
  <div class="tiny" style="left:25px;top:133px;width:285px">Our products seek to generate returns in a wide range of markets without any preference for Asset Class or Market Direction (Long or Short). The investment team has a solid track record, and generated Alpha at the Interest Rates, Currency and Stock Markets.</div>
  <div class="tiny" style="left:25px;top:149px;width:285px">The investment universe is mainly made by: Brazil, Emerging Markets and the major economies such as USA, Japan and Europe.</div>
  <div class="brand">BRENLO CAPITAL</div>
</section>

<section class="slide c2 r2">
  <div class="titlebox left"><span class="flag" style="background:var(--blue)"></span>Click to add title</div>
  <div class="photo sky" role="img" aria-label="City skyline with glass-domed station" style="left:0;top:38px;width:330px;height:64px"></div>
  <div class="label-tab" style="left:56px;top:111px;width:50px;background:var(--navy)">A</div>
  <div class="label-tab" style="left:110px;top:111px;width:50px;background:#3a3f44">B</div>
  <div class="label-tab" style="left:165px;top:111px;width:50px;background:var(--sky)">C</div>
  <div class="label-tab" style="left:219px;top:111px;width:50px;background:#7a7f84">D</div>
  <div class="tiny" style="left:58px;top:122px;width:48px">This product uses the same analysis of the MACRO Fund but higher leverage. It is focused on Long Term results.</div>
  <div class="tiny" style="left:112px;top:122px;width:48px">This product uses the same analysis of the MACRO Fund but higher leverage. It is focused on Long Term results.</div>
  <div class="tiny" style="left:167px;top:122px;width:48px">This product uses the same analysis of the MACRO Fund but higher leverage. It is focused on Long Term results.</div>
  <div class="tiny" style="left:221px;top:122px;width:48px">This product uses the same analysis of the MACRO Fund but higher leverage. It is focused on Long Term results.</div>
  <div class="brand">BRENLO CAPITAL</div>
</section>

<section class="slide c3 r2">
  <div class="titlebox right"><span class="flag" style="background:#888"></span>Click to add title</div>
  <div style="left:0;top:38px;width:330px;height:93px;background:var(--sky)"></div>
  <div class="photo" role="img" aria-label="City view tinted blue" style="left:0;top:38px;width:170px;height:93px;background:linear-gradient(90deg,rgba(120,160,190,.55),rgba(47,159,224,0))"></div>
  <div class="white" style="left:170px;top:50px;font-size:7.6px;font-weight:700">BRENLO ADVANCED</div>
  <div class="tiny white" style="left:170px;top:65px;width:150px;line-height:9px">This product uses the same analysis of the MACRO<br>This product uses the same analysis of the MACRO<br>This product uses the same analysis of the MACRO<br>This product uses the same analysis of the MACRO<br>This product uses the same analysis of the MACRO</div>
  <div class="brand">BRENLO CAPITAL</div>
</section>

<section class="slide c1 r3">
  <div class="titlebox left"><span class="flag"></span>Click to add title</div>
  <div class="photo sky" role="img" aria-label="City skyline with glass-domed station" style="left:0;top:46px;width:330px;height:94px"></div>
  <div style="left:50px;top:46px;width:70px;height:94px;background:var(--sky)"></div>
  <div class="white" style="left:56px;top:52px;width:62px;font-size:6px;line-height:9.8px">This product uses the same analysis of the MACRO Fund but higher leverage. It is focused on Long Term results.</div>
  <div class="brand">BRENLO CAPITAL</div>
</section>

<section class="slide c2 r3" style="background:linear-gradient(180deg,var(--sky),#1a7ec6)">
  <div class="brand light" style="left:57px;top:98px;bottom:auto;transform:none;font-size:10px">BRENLO CAPITAL</div>
  <div class="white" style="left:77px;top:120px;width:180px;font-size:6.2px;line-height:8px">This product uses the same analysis of the MACRO Fund but higher leverage. It is focused on Long Term results.</div>
</section>

<section class="slide c3 r3">
  <div class="titlebox right"><span class="flag"></span>Click to add title</div>
  <div class="photo sky" role="img" aria-label="Residential building" style="left:23px;top:42px;width:83px;height:60px"></div>
  <div class="photo sky" role="img" aria-label="Residential building" style="left:124px;top:42px;width:83px;height:60px"></div>
  <div class="photo sky" role="img" aria-label="Residential building" style="left:225px;top:42px;width:83px;height:60px"></div>
  <div class="label-tab" style="left:23px;top:102px;width:83px;background:var(--blue)">A</div>
  <div class="label-tab" style="left:124px;top:102px;width:83px;background:var(--blue)">B</div>
  <div class="label-tab" style="left:225px;top:102px;width:83px;background:var(--blue)">C</div>
  <div class="small" style="left:25px;top:112px;width:78px">This product uses the same analysis of the MACRO Fund but higher leverage. It is focused on Long Term results</div>
  <div class="small" style="left:126px;top:112px;width:78px">This product uses the same analysis of the MACRO Fund but higher leverage. It is focused on Long Term results It is focused on Long Term results</div>
  <div class="small" style="left:227px;top:112px;width:78px">This product uses the same analysis of the MACRO Fund but higher leverage. It is focused on Long Term results</div>
  <div class="brand">BRENLO CAPITAL</div>
</section>

<section class="slide c1 r4">
  <div class="titlebox right"><span class="flag"></span>Click to add title</div>
  <div class="photo" role="img" aria-label="Office building with trees" style="left:23px;top:40px;width:102px;height:99px;border-bottom:3px solid var(--blue)"></div>
  <div class="small" style="left:137px;top:47px;width:175px">This product uses the same analysis of the MACRO Fund but higher leverage. It is focused on Long Term results.</div>
  <div style="left:137px;top:62px;width:177px;height:1px;background:#9cc9e6"></div>
  <div class="small" style="left:137px;top:67px;width:175px">This product uses the same analysis of the MACRO Fund but higher leverage. It is focused on Long Term results. This product uses the same analysis of the MACRO Fund but higher leverage. It is focused on Long Term results.</div>
  <div style="left:137px;top:100px;width:177px;height:1px;background:#9cc9e6"></div>
  <div class="small" style="left:139px;top:121px;width:175px">This product uses the same analysis of the MACRO Fund but higher leverage. It is focused on Long Term results.</div>
  <div style="left:137px;top:139px;width:177px;height:1px;background:#9cc9e6"></div>
  <div class="brand">BRENLO CAPITAL</div>
</section>

<section class="slide c2 r4">
  <div class="heading"><span class="tab grey"></span><span>OUR SERVICE</span></div>
  <div style="left:170px;top:40px;width:1px;height:100px;background:var(--line)"></div>
  <div class="svc" style="left:20px;top:45px;text-align:right"><b>SERVICE</b>This product uses the same analysis of the MACRO Fund but higher leverage. It is focused on Long Term results.</div>
  <div class="svc" style="left:20px;top:72px;text-align:right"><b>SERVICE</b>This product uses the same analysis of the MACRO Fund but higher leverage. It is focused on Long Term results.</div>
  <div class="svc" style="left:20px;top:99px;text-align:right"><b>SERVICE</b>This product uses the same analysis of the MACRO Fund but higher leverage. It is focused on Long Term results.</div>
  <div class="svc" style="left:20px;top:126px;text-align:right"><b>SERVICE</b>This product uses the same analysis of the MACRO Fund but higher leverage. It is focused on Long Term results.</div>
  <div class="icon" style="left:137px;top:44px"><svg width="10" height="10"><rect x="1" y="5" width="2" height="4" fill="#fff"/><rect x="4" y="2" width="2" height="7" fill="#fff"/><rect x="7" y="4" width="2" height="5" fill="#fff"/></svg></div>
  <div class="icon" style="left:137px;top:71px"><svg width="10" height="10"><path d="M1 5 L9 2 L6 9 L5 6Z" fill="#fff"/></svg></div>
  <div class="icon" style="left:137px;top:98px"><svg width="10" height="10"><ellipse cx="5" cy="4.5" rx="4" ry="3.2" fill="#fff"/><path d="M3 7 L2 9.5 L5 7.5Z" fill="#fff"/></svg></div>
  <div class="icon" style="left:137px;top:125px"><svg width="10" height="10"><circle cx="4" cy="4" r="2.6" fill="none" stroke="#fff" stroke-width="1.4"/><path d="M6 6 L9 9" stroke="#fff" stroke-width="1.6"/></svg></div>
  <div class="icon" style="left:180px;top:44px"><svg width="10" height="10"><rect x="2" y="2" width="6" height="6" fill="#fff"/></svg></div>
  <div class="icon" style="left:180px;top:71px"><svg width="10" height="10"><circle cx="5" cy="5" r="4" fill="none" stroke="#fff"/><path d="M1 5H9M5 1V9" stroke="#fff" stroke-width=".8"/></svg></div>
  <div class="icon" style="left:180px;top:98px"><svg width="10" height="10"><path d="M2 8 L8 2M2 2 L8 8" stroke="#fff" stroke-width="1.3"/></svg></div>
  <div class="icon" style="left:180px;top:125px"><svg width="10" height="10"><circle cx="5" cy="4" r="3" fill="#fff"/><rect x="3.8" y="7" width="2.4" height="2" fill="#fff"/></svg></div>
  <div class="svc" style="left:205px;top:45px"><b>SERVICE</b>This product uses the same analysis of the MACRO Fund but higher leverage. It is focused on Long Term results.</div>
  <div class="svc" style="left:205px;top:72px"><b>SERVICE</b>This product uses the same analysis of the MACRO Fund but higher leverage. It is focused on Long Term results.</div>
  <div class="svc" style="left:205px;top:99px"><b>SERVICE</b>This product uses the same analysis of the MACRO Fund but higher leverage. It is focused on Long Term results.</div>
  <div class="svc" style="left:205px;top:126px"><b>SERVICE</b>This product uses the same analysis of the MACRO Fund but higher leverage. It is focused on Long Term results.</div>
  <div class="brand">BRENLO CAPITAL</div>
</section>

<section class="slide c3 r4">
  <div class="titlebox right"><span class="flag"></span>Click to add title</div>
  <div class="small" style="left:24px;top:54px;width:125px">This product uses the same analysis of the MACRO Fund but higher leverage. It is focused on Long Term results. This product uses the same analysis of the MACRO Fund but higher leverage. It is focused on Long Term results.</div>
  <div class="small" style="left:24px;top:94px;width:125px">This product uses the same analysis of the MACRO Fund but higher leverage. It is focused on Long Term results. This product uses the same analysis of the MACRO Fund but higher leverage. It is focused on Long Term results.</div>
  <div class="small" style="left:24px;top:134px;width:125px">This product uses the same analysis of the MACRO Fund but higher leverage. It is focused</div>
  <svg width="140" height="100" style="left:172px;top:45px">
    <path d="M6 2V96H140" fill="none" stroke="#999" stroke-width=".6"/>
    <polyline fill="none" stroke="var(--blue)" stroke-width=".9" points="12,20 15,12 18,22 21,8 24,30 27,45 30,40 33,55 36,50 39,62 42,58 45,70 48,60 51,68 54,56 57,72 60,52 63,62 66,48 69,20 72,58 75,70 78,62 81,55 84,65 87,52 90,68 93,60 96,74 99,66 102,72 105,64 108,70 111,76 114,72 117,78 120,74 123,80 126,76 129,80"/>
  </svg>
  <div class="brand">BRENLO CAPITAL</div>
</section>

<section class="slide c1 r5">
  <div class="photo tinted" role="img" aria-label="Office building tinted blue" style="left:0;top:0;width:108px;height:186px"></div>
  <div class="titlebox right" style="width:200px"><span class="flag"></span>Click to add title</div>
  <div style="left:119px;top:40px;font-size:6.2px;font-weight:700">MACRO</div>
  <div class="small" style="left:119px;top:56px;width:195px">This product uses the same analysis of the MACRO Fund but higher leverage. It is focused on Long Term results. This product uses the same analysis of the MACRO Fund but higher leverage. It is focused on Long Term results.</div>
  <div class="small" style="left:119px;top:92px;width:195px">This product uses the same analysis of the MACRO Fund but higher leverage. It is focused on Long Term results. This product uses the same analysis of the MACRO Fund but higher leverage. It is focused</div>
  <div class="icon" style="left:149px;top:122px;background:var(--blue)"><svg width="10" height="10"><rect x="2" y="2" width="6" height="6" fill="#fff"/></svg></div>
  <div class="svc" style="left:179px;top:122px;width:80px"><b>SERVICE</b>This product uses the same analysis of the MACRO Fund</div>
  <div class="icon" style="left:149px;top:148px;background:var(--blue)"><svg width="10" height="10"><rect x="2" y="2" width="6" height="6" fill="#fff"/></svg></div>
  <div class="svc" style="left:179px;top:148px;width:80px"><b>SERVICE</b>This product uses the same analysis of the MACRO Fund</div>
  <div class="brand" style="left:217px">BRENLO CAPITAL</div>
</section>

<section class="slide c2 r5">
  <div class="photo dark" role="img" aria-label="Office building in dark tones" style="left:25px;top:0;width:102px;height:186px"></div>
  <div class="titlebox right" style="width:180px"><span class="flag"></span>Click to add title</div>
  <div class="white" style="left:29px;top:46px;font-size:6.2px;font-weight:700">MACRO</div>
  <div class="small white" style="left:29px;top:60px;width:94px">This product uses the same analysis of the MACRO Fund but higher leverage. It is focused on Long Term results. This product uses the same analysis of the MACRO Fund but higher leverage. It is focused on Long Term results.</div>
  <div class="small white" style="left:29px;top:118px;width:94px">This product uses the same analysis of the MACRO Fund but higher leverage. It is focused on Long Term results. This product uses the same analysis. It is focused</div>
  <svg width="170" height="110" style="left:140px;top:45px">
    <path d="M14 2V106H168" fill="none" stroke="#999" stroke-width=".6"/>
    <polyline fill="none" stroke="var(--blue)" stroke-width=".9" points="20,22 24,12 28,28 32,16 36,40 40,55 44,48 48,62 52,58 56,72 60,66 64,78 68,70 72,80 76,64 80,74 84,60 88,30 92,70 96,82 100,72 104,66 108,76 112,62 116,74 120,70 124,82 128,76 132,84 136,78 140,86 144,82 148,88 152,84 156,88"/>
  </svg>
  <div class="brand" style="left:215px">BRENLO CAPITAL</div>
</section>

<section class="slide c3 r5">
  <div class="photo" role="img" aria-label="Business handshake" style="left:0;top:26px;width:330px;height:160px;background:linear-gradient(90deg,#2e3a45 0%,#6d7f8c 40%,#c79e86 65%,#8a9aa6 100%)"></div>
  <div style="left:42px;top:0;width:88px;height:186px;background:var(--sky)"></div>
  <div class="brand light" style="left:49px;top:13px;bottom:auto;transform:none;font-size:7px">BRENLO CAPITAL</div>
  <div class="white" style="left:42px;top:83px;width:88px;text-align:center;font-size:7.5px;font-weight:700">THANK YOU</div>
</section>

</body>
</html>
```